Business Card Design for TrailReady

TrailReady is an online e-commerce store specializing in Outdoors Gear such as camping equipment, hunting and shooting equipment, tactical gear and more. See complete line at trailready-gear.example
Logo: http://www.trailready-gear.example/media/ID/Ready.jpg
http://www.trailready-gear.example/media/ID/TrailReady-blue.jpg

Target Market(s)

20-40 Male

Industry/Entity Type

E-Commerce

```html
<!DOCTYPE html>
<html lang="en">
<head>
<meta charset="utf-8">
<title>TrailReady Business Card</title>
<link rel="stylesheet" href="https://fonts.googleapis.com/css2?family=Bitter:wght@700&family=Merriweather:wght@400;700&family=Open+Sans:wght@400;700&display=swap">
<style>
  :root {
    --navy: #0f3d66;
    --navy-text: #123b63;
    --paper: #ffffff;
    --ink: #2a2a2a;
    --backdrop: #eeeae6;
    --edge: #9a9a9a;
  }
  * { margin: 0; padding: 0; box-sizing: border-box; }
  html, body { width: 1200px; height: 900px; overflow: hidden; }
  body { background: var(--backdrop); position: relative; font-family: "Open Sans", Arial, sans-serif; }

  .card { position: absolute; top: 296px; width: 540px; height: 308px; }
  .card--front { left: 45px; background: var(--paper); border: 1px solid var(--edge); }
  .card--back { left: 617px; background: var(--navy); }

  /* front header */
  .brand { position: absolute; top: 30px; left: 93px; display: flex; align-items: center; gap: 10px; }
  .brand__dot { width: 48px; height: 48px; border-radius: 50%; border: 3px solid var(--navy); }
  .brand__name { font-family: "Bitter", Georgia, serif; font-weight: 700; font-size: 28px; color: var(--navy-text); letter-spacing: -0.2px; }
  .divider { position: absolute; width: 1.5px; background: var(--navy); }
  .card--front .divider { left: 418px; top: 26px; height: 76px; }
  .tagline { position: absolute; font-weight: 700; line-height: 1.35; }
  .card--front .tagline { left: 428px; top: 36px; font-size: 14.5px; color: var(--navy-text); }

  /* person */
  .person { position: absolute; left: 22px; top: 138px; font-family: "Merriweather", Georgia, serif; color: var(--navy-text); }
  .person__name { font-size: 25px; font-weight: 400; line-height: 1.05; }
  .person__role { font-size: 15px; margin-left: 14px; }

  /* contacts */
  .contacts { position: absolute; left: 22px; top: 203px; list-style: none; font-size: 11.5px; color: var(--ink); font-family: Arial, Helvetica, sans-serif; }
  .contacts li { display: flex; align-items: center; gap: 11px; height: 17.5px; }
  .contacts li.gap { margin-top: 7px; }
  .contacts svg { width: 12px; height: 12px; fill: var(--navy); flex: none; }
  .accent-bar { position: absolute; left: 0; bottom: 0; width: 193px; height: 9px; background: var(--navy); }

  /* back */
  .back-mark { position: absolute; left: 134px; top: 113px; width: 90px; height: 90px; border-radius: 50%; border: 3px solid var(--paper); }
  .card--back .divider { left: 241px; top: 96px; height: 122px; background: var(--paper); opacity: 0.8; }
  .card--back .tagline { left: 260px; top: 112px; font-size: 23px; line-height: 1.33; color: var(--paper); }
</style>
</head>
<body>
  <section class="card card--front" aria-label="Business card front">
    <div class="brand">
      <span class="brand__dot" aria-hidden="true"></span>
      <span class="brand__name">TrailReady.com</span>
    </div>
    <span class="divider"></span>
    <p class="tagline">Equipped for<br>Survival and<br>Adventure</p>

    <div class="person">
      <p class="person__name">John Doe</p>
      <p class="person__role">Director</p>
    </div>

    <ul class="contacts">
      <li><svg viewBox="0 0 12 12" aria-hidden="true"><path d="M2 1h6v10H2zM8 4h3v7H8z M3 2.5h1.5v1.5H3zM5.5 2.5H7v1.5H5.5zM3 5h1.5v1.5H3zM5.5 5H7v1.5H5.5z" fill-rule="evenodd"/></svg>(XXX) XXX-XXXX</li>
      <li><svg viewBox="0 0 12 12" aria-hidden="true"><path d="M1 4c0-2 2-2.5 5-2.5S11 2 11 4v1H8.5V3.8h-5V5H1zM3 6h6l1.5 4h-9z"/></svg>(XXX) XXX-XXXX - Direct</li>
      <li><svg viewBox="0 0 12 12" aria-hidden="true"><path d="M3.5 0.5h5v11h-5zM4.5 2v6h3V2z" fill-rule="evenodd"/></svg>(XXX) XXX-XXXX</li>
      <li class="gap"><svg viewBox="0 0 12 12" aria-hidden="true"><path d="M0.5 2h11v8h-11zM1.5 3v0.4L6 6.8l4.5-3.4V3zM1.5 4.6V9h9V4.6L6 8z" fill-rule="evenodd"/></svg>john@trailready-gear.example</li>
      <li><svg viewBox="0 0 12 12" aria-hidden="true"><path d="M6 0.5a5.5 5.5 0 1 0 0 11a5.5 5.5 0 1 0 0-11zM6 1.6c-1 1-1.6 2.6-1.6 4.4s0.6 3.4 1.6 4.4c1-1 1.6-2.6 1.6-4.4S7 2.6 6 1.6zM1.6 5.5h8.8v1H1.6z" fill-rule="evenodd"/></svg>trailready-gear.example</li>
    </ul>
    <span class="accent-bar"></span>
  </section>

  <section class="card card--back" aria-label="Business card back">
    <span class="back-mark" aria-hidden="true"></span>
    <span class="divider"></span>
    <p class="tagline">Equipped for<br>Survival and<br>Adventure</p>
  </section>
</body>
</html>
```